New Business Card Design Project

Need a design that will create an impact / strong impression towards our clients for our business. We are in the lighting business and we do lighting retrofits for large commercial to industrial clientele.

Target Market(s)

Lighting Industry

Industry/Entity Type

Business

Other font styles liked:
• we would like to use the font on our logo, not sure what it is though..

Requirements
Must have
• Our logo.
Nice to have
• We are open to suggestions that have to do with lighting.

```html
<!DOCTYPE html>
<html lang="en">
<head>
<meta charset="utf-8">
<title>Brightway Retrofit Group – Business Card</title>
<link rel="stylesheet" href="https://fonts.googleapis.com/css2?family=Open+Sans:wght@400;600;700&display=swap">
<style>
  :root {
    --bg: #e9eaec;
    --paper: #ffffff;
    --green-deep: #1f3d1f;
    --green-brand: #0e8445;
    --green-light: #6bbf59;
    --ink: #1f4d26;
    --grey: #6d6d6d;
    --rule: #8fd07a;
  }
  * { margin: 0; padding: 0; box-sizing: border-box; }
  html, body { width: 1200px; height: 800px; overflow: hidden; }
  body {
    background: var(--bg);
    font-family: "Open Sans", Arial, sans-serif;
    position: relative;
  }
  .card {
    position: absolute;
    top: 252px;
    width: 520px;
    height: 297px;
    overflow: hidden;
    box-shadow: 0 6px 18px rgba(0,0,0,0.12);
  }
  .card--front { left: 50px; background: var(--paper); }
  .card--back { left: 630px; background: var(--green-brand); }

  .accent-area { position: absolute; }
  .card--front .accent-area {
    right: 0; bottom: 0;
    width: 210px; height: 110px;
    background: linear-gradient(135deg, var(--green-light) 0%, var(--green-brand) 45%, var(--green-deep) 100%);
  }
  .card--back .accent-area {
    left: 0; top: 0;
    width: 120px; height: 297px;
    background: linear-gradient(90deg, var(--green-deep) 0%, var(--green-brand) 70%, var(--green-light) 100%);
  }

  .brand {
    position: absolute;
    display: flex;
    align-items: center;
    gap: 8px;
    font-weight: 700;
    font-size: 19px;
    letter-spacing: 0.02em;
    white-space: nowrap;
  }
  .brand__mark { width: 14px; height: 14px; flex: none; }
  .card--front .brand { left: 34px; top: 30px; color: var(--ink); }
  .card--front .brand__mark { background: var(--green-brand); }
  .card--back .brand { right: 30px; bottom: 42px; color: #ffffff; }
  .card--back .brand__mark { background: #ffffff; }

  .brand-rule {
    position: absolute;
    left: 34px; top: 64px;
    width: 250px; height: 1px;
    background: var(--green-brand);
  }

  .contact { position: absolute; left: 34px; top: 82px; width: 250px; }
  .contact__name {
    color: var(--ink);
    font-weight: 700;
    font-size: 18px;
    letter-spacing: 0.02em;
  }
  .contact__role { color: var(--grey); font-size: 12px; margin-bottom: 8px; }
  .contact__lines { color: var(--grey); font-size: 12px; line-height: 1.45; }
  .contact__rule { height: 1px; background: var(--rule); margin: 4px 0; }
</style>
</head>
<body>

<section class="card card--front" aria-label="Business card front">
  <div class="accent-area" role="img" aria-label="Corner accent in brand greens"></div>

  <div class="brand"><span class="brand__mark"></span>Brightway Retrofit Group</div>
  <div class="brand-rule"></div>

  <div class="contact">
    <p class="contact__name">JOHN DOE</p>
    <p class="contact__role">Director</p>
    <div class="contact__lines">
      <div class="contact__rule"></div>
      <p>+63 900 555 0147</p>
      <p>john@brightway.co | www.brightway.co</p>
      <p>Dummy Street, Dummy City</p>
      <p>Dummy Country</p>
      <div class="contact__rule"></div>
    </div>
  </div>
</section>

<section class="card card--back" aria-label="Business card back">
  <div class="accent-area" role="img" aria-label="Side accent in brand greens"></div>

  <div class="brand"><span class="brand__mark"></span>Brightway Retrofit Group</div>
</section>

</body>
</html>
```